Business Card for Veltrano, a french tech company

Tech company
New technologies
Serious design
Dark theme

User info :
Name: Mathis CORLAVE
Position: Co-Founder & CEO
Tel: (+33) 6 58 24 90 37
Email: mathis@veltrano.io
Website: www.veltrano.io
Address: 17 rue des Tanneurs 69002 LYON

Attached is the business logo file.

```html
<!DOCTYPE html>
<html lang="fr">
<head>
<meta charset="utf-8">
<title>Veltrano – Business Card</title>
<link rel="stylesheet" href="https://fonts.googleapis.com/css2?family=Rubik:wght@400;500;700&display=swap">
<style>
  :root {
    --stage: #2b2d30;
    --card: #0a1536;
    --card-edge: #101d45;
    --ink: #ffffff;
    --pink: #d93aa6;
    --violet: #8a4cc2;
    --blue: #1f84c4;
    --indigo: #2a2f8f;
  }
  * { box-sizing: border-box; margin: 0; padding: 0; }
  html, body {
    width: 1200px;
    height: 939px;
    overflow: hidden;
    background: var(--stage);
    font-family: "Rubik", Arial, sans-serif;
  }
  .stage {
    width: 1200px;
    height: 939px;
    display: flex;
    flex-direction: column;
    align-items: center;
    justify-content: center;
    gap: 56px;
  }
  .card {
    position: relative;
    width: 640px;
    height: 366px;
    background: var(--card);
    border: 1px solid var(--card-edge);
    border-radius: 4px;
    box-shadow: 0 18px 40px rgba(0, 0, 0, 0.45);
    overflow: hidden;
  }
  .card--front {
    display: flex;
    align-items: center;
    justify-content: center;
  }
  .wordmark {
    font-weight: 500;
    color: var(--violet);
    letter-spacing: 3px;
    text-transform: uppercase;
    line-height: 1;
  }
  .card--front .wordmark { font-size: 62px; }
  .card--back .wordmark {
    position: absolute;
    left: 48px;
    top: 58px;
    font-size: 46px;
  }
  .contact {
    position: absolute;
    left: 58px;
    top: 170px;
    color: var(--ink);
  }
  .contact__name {
    font-size: 25px;
    font-weight: 700;
    letter-spacing: 0.5px;
  }
  .contact__first { color: var(--pink); }
  .contact__last { color: var(--blue); font-weight: 500; }
  .contact__role {
    font-size: 14px;
    margin-top: 4px;
    margin-left: 14px;
  }
  .contact__address {
    font-size: 14px;
    line-height: 1.55;
    margin-top: 16px;
    margin-left: 28px;
    font-style: normal;
  }
  .contact__lines {
    list-style: none;
    margin-top: 14px;
    margin-left: 40px;
    font-size: 14px;
    line-height: 1.6;
  }
  .contact__lines li {
    display: flex;
    align-items: center;
    gap: 8px;
  }
  .contact__icon { width: 12px; height: 12px; flex: none; }
</style>
</head>
<body>
  <main class="stage">
    <section class="card card--front" aria-label="Recto">
      <span class="wordmark">Veltrano</span>
    </section>

    <section class="card card--back" aria-label="Verso">
      <span class="wordmark">Veltrano</span>
      <div class="contact">
        <p class="contact__name"><span class="contact__first">Mathis</span> <span class="contact__last">CORLAVE</span></p>
        <p class="contact__role">Co-Founder &amp; CEO</p>
        <address class="contact__address">17 rue des Tanneurs<br>69002 LYON</address>
        <ul class="contact__lines">
          <li>
            <svg class="contact__icon" viewBox="0 0 12 12" aria-hidden="true"><path d="M2.5 1 L4.5 1 L5.2 3.6 L4 4.6 C4.7 6 6 7.3 7.4 8 L8.4 6.8 L11 7.5 L11 9.5 C11 10.3 10.3 11 9.5 11 C5 11 1 7 1 2.5 C1 1.7 1.7 1 2.5 1 Z" fill="var(--pink)"/></svg>
            (+33) 6 58 24 90 37
          </li>
          <li>
            <svg class="contact__icon" viewBox="0 0 12 12" aria-hidden="true"><rect x="0.8" y="2.3" width="10.4" height="7.4" rx="1" fill="none" stroke="var(--pink)" stroke-width="1.3"/><path d="M1 2.8 L6 6.6 L11 2.8" fill="none" stroke="var(--blue)" stroke-width="1.3"/></svg>
            mathis@veltrano.io
          </li>
          <li>
            <svg class="contact__icon" viewBox="0 0 12 12" aria-hidden="true"><circle cx="6" cy="6" r="5" fill="none" stroke="var(--violet)" stroke-width="1.2"/><ellipse cx="6" cy="6" rx="2.2" ry="5" fill="none" stroke="var(--violet)" stroke-width="1"/><path d="M1 6 H11" stroke="var(--violet)" stroke-width="1"/></svg>
            www.veltrano.io
          </li>
        </ul>
      </div>
    </section>
  </main>
</body>
</html>
```